DATA PROTECTION OFFICER - GENERAL DATA PROTECTION REGULATION

Our network of companies is called : KVR (KVRL-MTO FLINTS).
It is sourced and based in Brussels, Belgium, hosting the EU institutions : designers and enforcers of the GDPR (https://portal.verimunda.example/info/norm/norm-topic/record-safety_en).
We are setting up connected, empowered and visionary-interconnected organizations in each country, region or city concerned by the GDPR.
We have developed unique pedagogical methods, programs, instruments (video, softwares,…) and visionary training skills – initially and on a continuous basis – for the DPO & GDPR consultants.
Our motto is : From Challenges to Opportunities.
Our yearning is : developing soulful teams, join forces & talents with our clients.
Our most wanted reward : let us astonish you!
We opt for the best available softwares on the market for project management, data analytics, GDPR compliance, DPO assistance and in general : customer relation and enhanced communication between project members.
We contribute to bringing Artificial Intelligence and Data-Driven Mindsets in enterprises.
We perceive the GDPR as the best opportunity an organization faces to value its “gold” (its data) and offer the solutions to transform them into real-life currencies and assets… MONEY .
I guess my comments need time to be integrated and I provided a lot of text too! I would particularly encourage TW (UK) to take the best out of his several proposals to mix them in the best ONE website! Offering me many graphic elements to use for all my posts/pages... I am a prolix writer :)
Target Market(s)
SME's business leaders, HR and Legal departments, read : https://www.corvanews.example/article/us-net-story-x1/growth-of-the-record-keeping-role-a-popular-new-career-path-idXQZT4LM8PW2K
Industry/Entity Type
Legal
Coding
Coded - Design and coding required
Number of Pages Required
5+ page
Colors
Designer to choose colors to be used in the design.
Requirements
Must have
- A HUMAN APPROACH
- WE NEED TO SEE HUMANS AND NOT ONLY ROBOTS OR ELECTRONIC DEVICES.
- 1) The DPO/GDPR Logos of the companies:
- https://www.filhaven.example/sh/k82q19wtzr4mn00/BXT7peLqVbZy0ghhwrR3Kslue?dl=0
- https://www.filhaven.example/sh/r3k27tjxwq85zmp/BXB4ktVRddh_q8ml5mtBgGqej?dl=0 et DPO : https://www.filhaven.example/sh/t9w4kjh7vcq48r2/BXJsmGZfRmYuvzIkwjR4Th_b?dl=0
- OR :
- https://www.filhaven.example/sh/vakkzp3mr5zgbn/BXBTxCRQ4lXmEFWN3LRg3kR7b?dl=0
- AND :
- https://stewardmesh.docushelf.example/sites/all/_layouts/15/visitorlink.aspx?visitortoken=Q4xbbe862KMTW7HkfaM5Wq0r%2BTcnNvdj1tqKX%2FmUmQOV%3D&folderid=3_2f70b91a29a805d81c96b8636e419f7ce&rev=1&e=6b600bf144535597b9296c99cd6116c9
- 2) A surprising but human, clear, simple, white, lightning look!
- 3) WORDPRESS version so that I can edit easily and add text on existing and new pages
- We therefore pass each option and - even more so - through the sieve of this inevitable - and values-generating - ethical evaluation.
- In other words, we are doubly satisfied with EVERY solution:
- 1. As a DPO/consultant and advisor to commercial enterprises or non-profit organisations but necessarily entering into a relationship involving financial flows with the persons concerned; and
- 2. As concerned person: target of the actions envisaged, parent, child, citizen and avatar in our digital lives.
- We put personal data at the centre of our projects and internal meetings, and with clients, we therefore continue the stage of brainstorming, researching and visualising ideas in interaction with the Regulation, by analysing the ethical consequences of each option.
- We choose only solutions that are applicable to the greatest number and therefore satisfy us as citizens of an increasingly connected and digital world. We also see the Regulation as a commercial and marketing opportunity to enhance the value of personal data and develop the confidence of those concerned by respect and security in the processing of such data.
- Our ultimate test: we put ourselves in our children's shoes to test the option considered, then comment on it and evaluate it as a parent.
- NO TO INCOMPREHENSIVE LEGAL TERMS... It is simply prohibited from 25 May for all information to be communicated to the persons concerned by the Regulation!
Nice to have
- - Artificial Intelligence
- - Transhumans
- - Challenges becoming Opportunities
- - a Great Dame who Protects & Reassures (see GDPR logo)
- - Friendly communication - NOT too businesslike/cold/usual
- - Page content is available here in FRENCH then ENGLISH then DUTCH then GERMAN : https://www.filhaven.example/sh/w1hjqmzsa101zwv/BXDNsFZpQSEzpMjhvRr5ZCb?dl=0
Should not have
- A cold, bankerlike, old economy, dull outlook

```html
<!DOCTYPE html>
<html lang="en">
<head>
<meta charset="utf-8">
<title>KVR – Data Protection Officer</title>
<link rel="stylesheet" href="https://fonts.googleapis.com/css2?family=Poppins:wght@300;400;500;600;700&display=swap">
<style>
:root{
  --navy:#1f2c7c;
  --navy-deep:#1a2566;
  --yellow:#f7d417;
  --ink:#3b3b3b;
  --muted:#555a66;
  --topbar:#2f2f2f;
  --light:#f4f4f4;
  --ring:#eeeeee;
  --disc:#dcdcdc;
  --white:#ffffff;
}
*{box-sizing:border-box;margin:0;padding:0}
html,body{width:1200px;height:3758px;overflow:hidden}
body{font-family:'Poppins',sans-serif;color:var(--ink);background:var(--white);position:relative}
.abs{position:absolute}

/* top bar */
.topbar{position:absolute;left:0;top:0;width:1200px;height:38px;background:var(--topbar)}
.social{position:absolute;left:112px;top:11px;display:flex;gap:20px}
.social span{width:16px;height:16px;border-radius:50%;background:#fff;display:block}
.lang{position:absolute;left:955px;top:11px;color:#fff;font-size:11px;font-weight:500}
.login{position:absolute;left:1002px;top:0;width:118px;height:38px;background:var(--navy);color:#fff;font-size:11px;font-weight:600;display:flex;align-items:center;justify-content:center}

/* header */
.header{position:absolute;left:0;top:38px;width:1200px;height:100px;background:#fff}
.brand{position:absolute;left:112px;top:30px;display:flex;align-items:center;gap:12px}
.brand-dot{width:36px;height:36px;border-radius:50%;background:var(--yellow)}
.brand-name{font-size:30px;font-weight:600;color:var(--navy);letter-spacing:1px}
.nav a{position:absolute;top:43px;font-size:13px;font-weight:500;color:var(--navy);text-decoration:none}

/* hero */
.hero{position:absolute;left:0;top:138px;width:1200px;height:490px;overflow:hidden}
.hero-photo{position:absolute;inset:0;background:radial-gradient(ellipse at 50% 45%,#8a8a8a 0%,#4a4a4a 40%,#1d1d1d 80%)}
.hero-tag{position:absolute;left:0;top:316px;width:1200px;text-align:center;color:#fff;font-size:18px;font-weight:500}
.btn-yellow{background:var(--yellow);color:var(--navy-deep);font-weight:600;border-radius:30px;display:flex;align-items:center;justify-content:center}
.hero-btn{position:absolute;left:481px;top:383px;width:238px;height:58px;font-size:14px}
.hero-curve{position:absolute;left:0;bottom:0}

/* intro */
.intro{position:absolute;left:0;top:626px;width:1200px;height:677px;background:var(--light)}
.intro-text{position:absolute;left:112px;top:92px;width:973px;text-align:center;font-size:11.5px;line-height:21px;color:var(--muted)}
.card{position:absolute;top:231px;width:299px;height:371px;background:#fff;box-shadow:0 2px 8px rgba(0,0,0,.12);text-align:center}
.card h3{margin-top:42px;font-size:17px;font-weight:500;color:var(--navy)}
.card-icon{width:78px;height:78px;border-radius:50%;border:1px solid #d6d6d6;margin:22px auto 0;display:flex;align-items:center;justify-content:center}
.card p{margin:28px auto 0;width:232px;font-size:11.5px;line-height:19px;color:var(--muted)}
.btn-outline{display:inline-flex;margin-top:26px;width:112px;height:35px;border:2px solid var(--yellow);border-radius:20px;align-items:center;justify-content:center;font-size:10px;font-weight:500;color:var(--ink)}

/* how it works */
.section-title{position:absolute;left:0;width:1200px;text-align:center;font-size:26px;font-weight:500;color:var(--navy)}
.step-title{position:absolute;font-size:16px;font-weight:600;color:var(--navy)}
.step-text{position:absolute;font-size:11.5px;line-height:20px;color:var(--muted)}
.step-text p{margin-bottom:8px}
.step-disc{position:absolute;width:276px;height:276px;border-radius:50%;background:#fff;border:14px solid var(--ring);display:flex;align-items:center;justify-content:center}
.step-disc .inner{width:228px;height:228px;border-radius:50%;background:var(--disc);display:flex;align-items:center;justify-content:center}
.badge{position:absolute;width:40px;height:40px;border-radius:50%;background:var(--yellow);color:var(--navy-deep);font-size:16px;font-weight:600;display:flex;align-items:center;justify-content:center}

/* video */
.video{position:absolute;left:0;top:2685px;width:1200px;height:451px;background:linear-gradient(135deg,#2a3a95 0%,#1f2c7c 50%,#17215e 100%)}
.play{position:absolute;left:576px;top:201px}

/* contact */
.map{position:absolute;left:112px;top:3294px;width:514px;height:200px;background:linear-gradient(160deg,#b9d6ee 0%,#d9e6d4 55%,#c7d9ea 100%)}
.contact-line{position:absolute;left:112px;display:flex;gap:14px;font-size:12px;line-height:19px;color:var(--muted)}
.contact-line svg{flex:none;margin-top:2px}
.contact-phone{font-size:19px;font-weight:600;color:var(--navy)}
.form-brand{position:absolute;left:676px;top:3300px;display:flex;align-items:center;gap:10px}
.form-brand .brand-dot{width:30px;height:30px}
.form-brand .brand-name{font-size:26px}
.field{position:absolute;left:676px;width:411px;border:1px solid #e0e0e0;font-size:10.5px;color:var(--muted);padding:8px 10px}
.form-btn{position:absolute;left:676px;top:3620px;width:106px;height:32px;font-size:10px}

/* footer */
.footer{position:absolute;left:0;top:3697px;width:1200px;height:61px;background:var(--navy)}
.footer-copy{position:absolute;left:150px;top:22px;font-size:11px;color:#fff}
.footer a{position:absolute;top:22px;font-size:11px;color:#fff;text-decoration:none}
</style>
</head>
<body>

<div class="topbar">
  <div class="social"><span></span><span></span><span></span><span></span></div>
  <div class="lang">EN ▾</div>
  <div class="login">LOGIN</div>
</div>

<header class="header">
  <div class="brand"><span class="brand-dot"></span><span class="brand-name">KVR</span></div>
  <nav class="nav">
    <a style="left:696px">HOME</a>
    <a style="left:768px">ABOUT</a>
    <a style="left:846px">SERVICES</a>
    <a style="left:940px">NEWS</a>
    <a style="left:1013px">CONTACT</a>
  </nav>
</header>

<section class="hero">
  <div class="hero-photo" role="img" aria-label="Black and white photo of hands framing the word privacy written in chalk"></div>
  <p class="hero-tag">Empowered And Visionary-Interconnected Organizations In Each Country,</p>
  <div class="btn-yellow hero-btn">GET STARTED NOW</div>
  <svg class="hero-curve" width="1200" height="40" viewBox="0 0 1200 40">
    <path d="M0 12 Q600 44 1200 12 L1200 40 L0 40 Z" fill="#d8d8d8"/>
    <path d="M0 18 Q600 46 1200 18 L1200 40 L0 40 Z" fill="var(--light)"/>
  </svg>
</section>

<section class="intro">
  <p class="intro-text">Lorem ipsum dolor sit amet, consectetuer adipiscing elit, sed diam nonummy nibh euismod tincidunt ut laoreet dolore magna aliquam erat volutpat. Ut wisi enim ad minim veniam, quis nostrud exerci tation ullamcorper suscipit lobortis nisl ut aliquip ex ea commodo consequat. Duis autem vel eum iriure dolor in hendrerit in vulputate velit esse molestie consequat, vel illum dolore eu feugiat nulla facilisis at vero eros et accumsan et iusto odio dignissim qui blandit praesent luptatum zzril delenit augue duis dolore te feugait nulla facilisi.</p>

  <div class="card" style="left:112px">
    <h3>LEGAL DESIGN</h3>
    <div class="card-icon"><svg width="40" height="40" viewBox="0 0 40 40" fill="none" stroke="var(--navy)" stroke-width="1.8"><path d="M8 14 L22 8 L32 13 L32 28 L18 34 L8 29 Z"/><path d="M8 14 L18 19 L32 13 M18 19 L18 34"/></svg></div>
    <p>Lorem ipsum dolor sit amet, consetadipiscing elit, sed diam nonummy nibh euismod tincidunt ut laoreet dolore magna aliquam erat volutpat. Ut wisi enim.</p>
    <span class="btn-outline">READ MORE</span>
  </div>
  <div class="card" style="left:451px">
    <h3>ARTIFICIAL INTELLIGENCE</h3>
    <div class="card-icon"><svg width="40" height="40" viewBox="0 0 40 40" fill="none" stroke="var(--navy)" stroke-width="1.8"><circle cx="20" cy="20" r="13"/><circle cx="20" cy="20" r="4"/><path d="M20 7 V16 M20 24 V33 M7 20 H16 M24 20 H33"/></svg></div>
    <p>Lorem ipsum dolor sit amet, consetadipiscing elit, sed diam nonummy nibh euismod tincidunt ut laoreet dolore magna aliquam erat volutpat. Ut wisi enim.</p>
    <span class="btn-outline">READ MORE</span>
  </div>
  <div class="card" style="left:789px">
    <h3>ETHICS OR "HUMAN BY DESIGN"</h3>
    <div class="card-icon"><svg width="40" height="40" viewBox="0 0 40 40" fill="none" stroke="var(--navy)" stroke-width="1.8"><rect x="12" y="18" width="16" height="14" rx="2"/><path d="M15 18 V13 a5 5 0 0 1 10 0 V18"/><circle cx="20" cy="25" r="2"/></svg></div>
    <p>Lorem ipsum dolor sit amet, consetadipiscing elit, sed diam nonummy nibh euismod tincidunt ut laoreet dolore magna aliquam erat volutpat. Ut wisi enim.</p>
    <span class="btn-outline">READ MORE</span>
  </div>
</section>

<section class="how">
  <h2 class="section-title" style="top:1390px">HERE'S HOW IT WORKS</h2>

  <h3 class="step-title" style="left:112px;top:1476px">GRAPHIC TABLE &amp; INTERACTION</h3>
  <div class="step-text" style="left:112px;top:1514px;width:650px">
    <p>The 3 profiles of our teams (IT/cybersecurity Expert – Lawyer – Project Manager) make use of modern tools of communication INTERNALLY and EXTERNALLY with external clients and partners.</p>
    <p>We use tactile tablets and graphic applications for drawing, mind-mapping, visualization, advanced natural language generation (advanced NLG), video, storytelling...</p>
    <p>We draw and "sketch" – without the slightest intention that the result be aesthetic and communicable as it is and at this stage to the different recipients (see step 3 to achieve this result).</p>
    <p>A diagram, a graph, an icon, steps, a process, sanctions or not depending on the choices made, measurable and quantified financial benefits, gains in terms of reputation, data analysis and marketing or communication operations...</p>
  </div>
  <div class="step-disc" style="left:826px;top:1500px"><div class="inner">
    <svg width="110" height="90" viewBox="0 0 110 90" fill="none" stroke="var(--navy)" stroke-width="4"><rect x="10" y="15" width="80" height="62" rx="6"/><path d="M28 55 C34 35 40 60 48 42 S58 52 66 40"/><path d="M68 48 L98 10 L104 16 L74 54 Z" fill="var(--navy)"/></svg>
  </div></div>
  <div class="badge" style="left:1042px;top:1490px">1</div>
  <svg class="abs" style="left:990px;top:1724px" width="60" height="110" viewBox="0 0 60 110" fill="none" stroke="var(--yellow)" stroke-width="3"><path d="M48 4 C56 50 40 80 12 100"/><path d="M10 84 L10 102 L28 100"/></svg>

  <div class="step-disc" style="left:112px;top:1841px"><div class="inner">
    <svg width="90" height="110" viewBox="0 0 90 110" fill="none" stroke="var(--navy)" stroke-width="4"><rect x="18" y="8" width="60" height="80" rx="3"/><path d="M10 18 V100 H68"/><path d="M30 28 H66 M30 38 H56"/><path d="M28 74 L40 56 L50 66 L66 46"/></svg>
  </div></div>
  <div class="badge" style="left:110px;top:1879px">2</div>
  <h3 class="step-title" style="left:433px;top:1868px">HUMAN BY DESIGN</h3>
  <div class="step-text" style="left:433px;top:1906px;width:652px">
    <p>Each Solution passes a double test that satisfies us both :</p>
    <p>1. As a DPO/consultant and advisor to commercial enterprises or non-profit organizations but necessarily entering into a relationship involving financial flows with the persons concerned; and</p>
    <p>2. As a data subject : "target" of the envisaged actions, parent, child, citizen and avatar in our digital lives.</p>
    <p>We put personal data at the center of our projects and internal meetings, and with clients, we therefore continue the stage of brainstorming, researching and visualizing ideas in interaction with the Regulation, by analyzing the ethical consequences of each option.</p>
    <p>We only retain solutions that are applicable to the greatest number and therefore satisfy us as citizens of an increasingly connected and digital world. We also see the Regulation as a commercial and marketing opportunity to enhance the value of personal data and develop the confidence of those concerned by respect and security in the processing of such data.</p>
    <p>Our ultimate test: we put ourselves in our children's shoes to test the option considered, then comment on it and evaluate it as a parent.</p>
  </div>
  <svg class="abs" style="left:130px;top:2140px" width="70" height="100" viewBox="0 0 70 100" fill="none" stroke="var(--yellow)" stroke-width="3"><path d="M6 4 C8 40 26 70 56 88"/><path d="M40 90 L58 90 L54 72"/></svg>

  <h3 class="step-title" style="left:112px;top:2330px">VISUALIZATION AND REDACTION</h3>
  <div class="step-text" style="left:112px;top:2368px;width:650px">
    <p>During the first two stages, we prepared a desirable objective: Communicate visually after an ethical check. Two external solutions (human and artificial) will help us to finalise the communication in a professional and optimal way.</p>
    <p>We draw and "sketch" – without the slightest intention that the result be aesthetic and communicable as it is and at this stage to the different recipients (see step 3 to achieve this result).</p>
    <p>A diagram, a graph, an icon, steps, a process, sanctions or not depending on the choices made, measurable and quantified financial benefits, gains in terms of reputation, data analysis and marketing or communication operations...</p>
  </div>
  <div class="step-disc" style="left:826px;top:2329px"><div class="inner">
    <svg width="110" height="110" viewBox="0 0 110 110" fill="none" stroke="var(--navy)" stroke-width="4"><path d="M34 100 V82 C18 74 12 58 16 42 C22 18 46 8 66 14 C84 20 94 36 92 54 L100 68 L92 70 V84 H76 V100"/><path d="M44 48 L60 40 L76 48 V66 L60 74 L44 66 Z M44 48 L60 56 L76 48 M60 56 V74"/></svg>
  </div></div>
  <div class="badge" style="left:1040px;top:2345px">3</div>
</section>

<section class="video" role="img" aria-label="Blue-toned close-up photo of a keyboard with a privacy key">
  <svg class="play" width="50" height="50" viewBox="0 0 50 50" fill="none"><circle cx="25" cy="25" r="22" stroke="#fff" stroke-width="3"/><path d="M20 15 L35 25 L20 35 Z" fill="#fff"/></svg>
</section>

<section class="contact">
  <h2 class="section-title" style="top:3220px">CONTACT US</h2>
  <div class="map" role="img" aria-label="Map showing the office location"></div>

  <div class="contact-line" style="top:3512px">
    <svg width="14" height="18" viewBox="0 0 14 18"><path d="M7 0 C3 0 0 3 0 7 C0 12 7 18 7 18 C7 18 14 12 14 7 C14 3 11 0 7 0 Z" fill="var(--navy)"/><circle cx="7" cy="7" r="2.5" fill="#fff"/></svg>
    <div>Rue Valmontier 47<br>B-1270 Orvelle - Belgium<br>+3225550147</div>
  </div>
  <div class="contact-line" style="top:3592px">
    <svg width="14" height="12" viewBox="0 0 14 12"><rect width="14" height="11" rx="1" fill="var(--navy)"/><path d="M1 1 L7 6 L13 1" stroke="#fff" fill="none"/></svg>
    <div>info@kvr-flints.example</div>
  </div>
  <div class="contact-line" style="top:3624px;align-items:center">
    <svg width="14" height="14" viewBox="0 0 14 14"><path d="M3 0 L5 4 L3.5 5.5 C4.5 7.5 6.5 9.5 8.5 10.5 L10 9 L14 11 L12 14 C6 14 0 8 0 2 Z" fill="var(--navy)"/></svg>
    <div class="contact-phone">+3225550147</div>
  </div>

  <div class="form-brand"><span class="brand-dot"></span><span class="brand-name">KVR</span></div>
  <div class="field" style="top:3374px;height:33px">Name:</div>
  <div class="field" style="top:3420px;height:33px">Email:</div>
  <div class="field" style="top:3466px;height:33px">Phone:</div>
  <div class="field" style="top:3512px;height:86px">Message:</div>
  <div class="btn-yellow form-btn">READ MORE</div>
</section>

<footer class="footer">
  <div class="footer-copy">KVR DPO © All Rights Reserved. 2018</div>
  <a style="left:714px">Home</a>
  <a style="left:789px">About</a>
  <a style="left:869px">Services</a>
  <a style="left:960px">News</a>
  <a style="left:1038px">Contact</a>
</footer>

</body>
</html>
```